Slides for industrial furniture site

I am looking for three slides (1400x530) that will go on my homepage. All slides need to be simple and a projection of the goods i am selling.
The slides need to be up there in the design trends for 2014.
I prefer:
- One large photo in each slide, maybe faded with a product in the front.
- Some example text in different fonts.
- light coloured slides. That go well in white oriented site.
- pictures may include these products: https://www.findora-example.nl/search?q=morvane+lights
AND:
https://www.findora-example.nl/search?q=vintage+theatre+light
OR:
https://www.findora-example.nl/search?q=vintage+stools
OR:
https://www.findora-example.nl/search?q=brevak+chair#q=original%20brevak%20chair
Maybe one slide with an interior like this:
https://www.findora-example.nl/search?q=industrial+interiors
Just let me see your creations and take into account the above.
For some examples:
http://quietmarsh-example.co/
http://pixelhof-example.at/en/
https://www.fernandlamp-example.com/
http://www.ulvastudio-example.com/
http://quillbarrow-example.ca/en/
http://skinforge-example.com/
For some theory (sorry if this is offensive ;-):
http://www.deckvault-example.net/plumo/font-pairing-slides
http://www.deckvault-example.net/brightmill2014/web-design-trends-2014
http://www.deckvault-example.net/tobyrand/how-to-create-great-slides-for-presentations
I hope you can create great slides for me!
Thnx
Reason: Hi designers. I am still looking for the perfect three lsides. Could you please make a few more.
Greetings,
Harlem
Reason: Sorry designers.
I am waiting for some designs from specific designers.
Industrial

```html
<!DOCTYPE html>
<html lang="en">
<head>
<meta charset="utf-8">
<title>Morvane Light – Home Slide</title>
<link rel="stylesheet" href="https://fonts.googleapis.com/css2?family=Michroma&family=Indie+Flower&family=Questrial&display=swap">
<style>
  :root {
    --backdrop: #dcdcdc;
    --panel: #efefef;
    --title-blue: #3d63d6;
    --tagline-blue: #5a72b8;
    --rule: #6f7fb0;
    --icon-dark: #1c1c1c;
    --icon-ring: #cfcfcf;
    --icon-glyph: #ffffff;
    --label: #1e1e1e;
    --hero-pink: #f3d6e2;
    --hero-cyan: #bfe6ee;
    --hero-cream: #f4efe9;
    --hero-skirting: #c9bfb3;
    --hero-floor: #c3ccd9;
    --lamp-blue: #3559c8;
    --lamp-pink: #d42a9a;
    --lamp-red: #d0302e;
    --lamp-black: #2a2a2e;
  }
  * { margin: 0; padding: 0; box-sizing: border-box; }
  html, body {
    width: 1200px;
    height: 918px;
    overflow: hidden;
    background: var(--backdrop);
  }
  .homepage {
    position: absolute;
    top: 82px;
    left: 0;
    width: 1200px;
    height: 754px;
    overflow: hidden;
    background: var(--panel);
  }
  .hero {
    position: relative;
    width: 1200px;
    height: 453px;
    overflow: hidden;
  }
  .hero-photo {
    position: absolute;
    inset: 0;
    background:
      linear-gradient(180deg, rgba(255,255,255,0) 0%, rgba(255,255,255,0) 77%, var(--hero-skirting) 77.5%, var(--hero-skirting) 79%, var(--hero-floor) 79.5%, #d9dfe8 100%),
      linear-gradient(100deg, var(--hero-cyan) 0%, var(--hero-pink) 30%, var(--hero-cream) 55%, var(--hero-cyan) 78%, #f1d2cf 100%);
  }
  .hero-product {
    position: absolute;
    bottom: 22px;
    border-radius: 10px;
  }
  .hero-product--left {
    left: 150px;
    width: 250px;
    height: 330px;
    background: linear-gradient(90deg, var(--lamp-blue) 0%, #7a6fd0 50%, var(--lamp-pink) 100%);
    opacity: 0.55;
  }
  .hero-product--right {
    left: 860px;
    width: 340px;
    height: 400px;
    background: linear-gradient(90deg, var(--lamp-black) 0%, var(--lamp-red) 45%, #5a4a40 70%, var(--lamp-red) 100%);
    opacity: 0.5;
  }
  .hero-copy {
    position: absolute;
    left: 0;
    right: 0;
    top: 126px;
    text-align: center;
  }
  .hero-title {
    display: inline-block;
    font-family: 'Michroma', sans-serif;
    font-weight: 400;
    font-size: 36px;
    letter-spacing: 4px;
    color: var(--title-blue);
    padding: 4px 6px 2px;
    border-top: 1.5px solid var(--rule);
    border-bottom: 1.5px solid var(--rule);
    line-height: 1.3;
  }
  .hero-tagline {
    margin-top: 2px;
    font-family: 'Indie Flower', cursive;
    font-size: 19px;
    letter-spacing: 2.5px;
    line-height: 24px;
    color: var(--tagline-blue);
  }
  .features {
    position: relative;
    height: 301px;
  }
  .feature {
    position: absolute;
    top: 79px;
    width: 280px;
    margin-left: -140px;
    text-align: center;
    font-family: 'Questrial', sans-serif;
    color: var(--label);
  }
  .feature--contact { left: 225px; }
  .feature--faq { left: 644px; }
  .feature--blog { left: 1060px; }
  .feature-icon {
    display: block;
    width: 94px;
    height: 94px;
    margin: 0 auto 18px;
  }
  .feature-title {
    font-size: 13px;
    letter-spacing: 2px;
    line-height: 19px;
    text-transform: uppercase;
  }
  .feature-text {
    font-size: 13px;
    letter-spacing: 1.6px;
    line-height: 19px;
  }
</style>
</head>
<body>
  <main class="homepage">
    <section class="hero">
      <div class="hero-photo" role="img" aria-label="Bright pastel studio backdrop with soft light flares and a pale floor"></div>
      <div class="hero-product hero-product--left" role="img" aria-label="Product photo: blue and pink articulated desk lamps"></div>
      <div class="hero-product hero-product--right" role="img" aria-label="Product photo: black, red and grey articulated industrial lamps"></div>
      <div class="hero-copy">
        <h1 class="hero-title">MORVANE LIGHT</h1>
        <p class="hero-tagline">It is during our darkest moments<br>that we must focus to see the light</p>
      </div>
    </section>

    <section class="features">
      <svg width="0" height="0" style="position:absolute">
        <defs>
          <radialGradient id="iconShade" cx="40%" cy="30%" r="75%">
            <stop offset="0%" stop-color="#4a4a4a"/>
            <stop offset="100%" stop-color="#141414"/>
          </radialGradient>
        </defs>
      </svg>

      <a class="feature feature--contact">
        <svg class="feature-icon" viewBox="0 0 96 96" aria-hidden="true">
          <circle cx="48" cy="48" r="47" fill="var(--icon-ring)"/>
          <circle cx="48" cy="48" r="44" fill="url(#iconShade)"/>
          <rect x="32" y="22" width="32" height="52" rx="4" fill="var(--icon-glyph)"/>
          <rect x="36" y="27" width="24" height="16" fill="var(--icon-dark)"/>
          <g fill="var(--icon-dark)">
            <rect x="37" y="47" width="6" height="4"/><rect x="45" y="47" width="6" height="4"/><rect x="53" y="47" width="6" height="4"/>
            <rect x="37" y="54" width="6" height="4"/><rect x="45" y="54" width="6" height="4"/><rect x="53" y="54" width="6" height="4"/>
            <rect x="37" y="61" width="6" height="4"/><rect x="45" y="61" width="6" height="4"/><rect x="53" y="61" width="6" height="4"/>
          </g>
        </svg>
        <p class="feature-title">Contact Us</p>
        <p class="feature-text">Experienced Support Team</p>
      </a>

      <a class="feature feature--faq">
        <svg class="feature-icon" viewBox="0 0 96 96" aria-hidden="true">
          <circle cx="48" cy="48" r="47" fill="var(--icon-ring)"/>
          <circle cx="48" cy="48" r="44" fill="url(#iconShade)"/>
          <circle cx="42" cy="41" r="13" fill="none" stroke="var(--icon-glyph)" stroke-width="7"/>
          <line x1="52" y1="51" x2="66" y2="66" stroke="var(--icon-glyph)" stroke-width="10" stroke-linecap="round"/>
        </svg>
        <p class="feature-title">FAQ</p>
        <p class="feature-text">Troubleshooting</p>
      </a>

      <a class="feature feature--blog">
        <svg class="feature-icon" viewBox="0 0 96 96" aria-hidden="true">
          <circle cx="48" cy="48" r="47" fill="var(--icon-ring)"/>
          <circle cx="48" cy="48" r="44" fill="url(#iconShade)"/>
          <path d="M48 70 L28 50 C20 42 24 28 36 28 C42 28 46 32 48 36 C50 32 54 28 60 28 C72 28 76 42 68 50 Z" fill="var(--icon-glyph)"/>
        </svg>
        <p class="feature-title">Blog</p>
        <p class="feature-text">Red More On Our Blog</p>
      </a>
    </section>
  </main>
</body>
</html>
```